ad for food show brochure

Need to clean up this concept sketch. We are selling food at a festival but the concept isn't quite named. We're looking to create a buzz and have people sign up to be kept apprised of the progress of the chain ... or the first store. The website at the bottom is just for filler, we can add that before ad goes to print. We're not married to this text so if you come up with something better, great. also may want to have a blank @ line for twitter feed and another line for FB page.
The concept is for a Vegan Fast Food place but I need to focus more on the middle of the road diners, we'll get the vegans to come and staunch carnivores won't ever come so it's the middle of the road folks we're after. The slant and speed lines were my attempt to show speed.
Thanks.
This ad is a 5/5 x 2.125 space in the festival brochure. Need this asap.
I also think this needs to be b&w so lets go with that. Just found out COLOR is ok.
That last word in the sketch is not whose but WHERE?
The last word is WHERE not whose. Thanks
We either need to add the word Vegan in the top of the ad or add it in the sentence about all that is vegan and good in the worl.
The ad can be in color. Just to clarify, the word Vegan should be o e of the questions on top. Eithe as part of another question ... 'Vegan fast food?' Or as its own line or bubble.
- pdf file so I can change the website address.

```html
<!DOCTYPE html>
<html lang="en">
<head>
<meta charset="utf-8">
<title>Vegan Fast Food – Coming Soon</title>
<link rel="stylesheet" href="https://fonts.googleapis.com/css2?family=Archivo+Black&family=Lilita+One&family=Gochi+Hand&family=Varela+Round&family=Arimo:ital,wght@1,700&display=swap">
<style>
  :root {
    --board: #231f20;
    --lime: #c9d52b;
    --white: #ffffff;
    --magenta: #e5097f;
    --sky: #1b9bd7;
    --orange: #f29a22;
    --red: #e3231b;
    --band: #fbbd29;
    --ink: #231f20;
  }
  html, body {
    margin: 0;
    padding: 0;
    width: 1200px;
    height: 2866px;
    overflow: hidden;
    background: var(--board);
  }
  .ad {
    position: relative;
    width: 1200px;
    height: 2866px;
    background: var(--board);
    overflow: hidden;
  }
  .speed-lines {
    position: absolute;
    left: 0;
    top: 0;
  }
  .headline {
    position: absolute;
    margin: 0;
    font-family: "Archivo Black", "Arial Black", sans-serif;
    color: var(--lime);
    font-size: 205px;
    line-height: 1;
    letter-spacing: -4px;
    transform: skewX(-16deg) rotate(-4deg);
    transform-origin: left bottom;
    white-space: nowrap;
  }
  .headline--vegan { left: 250px; top: 120px; }
  .headline--fast  { left: 420px; top: 310px; }
  .headline--food  { left: 120px; top: 500px; font-size: 215px; }

  .yep {
    position: absolute;
    font-family: "Gochi Hand", cursive;
    color: var(--white);
    font-size: 82px;
    line-height: 1;
  }
  .yep--food   { left: 890px; top: 780px; }
  .yep--soon   { left: 885px; top: 1110px; }
  .yep--nyc    { left: 870px; top: 1320px; }

  .question {
    position: absolute;
    margin: 0;
    line-height: 1;
    white-space: nowrap;
  }
  .question--soon {
    left: 85px;
    top: 990px;
    font-family: "Lilita One", "Arial Black", sans-serif;
    font-weight: 400;
    font-size: 138px;
    letter-spacing: 1px;
    color: var(--magenta);
    transform: rotate(-5deg);
    transform-origin: left bottom;
  }
  .question--nyc {
    left: 270px;
    top: 1255px;
    font-family: "Archivo Black", "Arial Black", sans-serif;
    font-size: 132px;
    color: var(--sky);
    transform: rotate(-3deg) skewX(-6deg);
  }

  .plea {
    position: absolute;
    left: 110px;
    top: 1470px;
    margin: 0;
    text-align: left;
    white-space: nowrap;
    font-family: "Arimo", Arial, sans-serif;
    font-style: italic;
    font-weight: 700;
    font-size: 78px;
    line-height: 1.08;
    color: var(--orange);
    transform: rotate(-4deg);
    transform-origin: left top;
  }
  .plea__where {
    display: block;
    margin-top: 10px;
    margin-left: 50px;
    font-size: 150px;
    line-height: 1;
    color: var(--red);
    letter-spacing: 4px;
  }

  .contact-band {
    position: absolute;
    left: 0;
    top: 1930px;
    width: 1200px;
    height: 350px;
    background: var(--band);
    color: var(--ink);
    font-family: "Varela Round", Arial, sans-serif;
  }
  .contact-band__site {
    position: absolute;
    top: 28px;
    left: 0;
    width: 100%;
    text-align: center;
    font-size: 74px;
    line-height: 1;
    margin: 0;
  }
  .contact-band__site b { font-weight: 700; }
  .contact-band__rule {
    position: absolute;
    left: 100px;
    top: 122px;
    width: 1000px;
    height: 5px;
    background: var(--ink);
  }
  .social {
    position: absolute;
    left: 0;
    width: 100%;
    display: flex;
    justify-content: center;
    align-items: center;
    gap: 22px;
    font-size: 68px;
    line-height: 1;
    margin: 0;
  }
  .social--one { top: 152px; }
  .social--two { top: 250px; }
  .social__mark {
    width: 66px;
    height: 66px;
    background: var(--ink);
    border-radius: 6px;
  }

  .until {
    position: absolute;
    margin: 0;
    font-family: "Varela Round", Arial, sans-serif;
    color: var(--white);
    font-size: 86px;
    letter-spacing: 3px;
    line-height: 1;
    white-space: nowrap;
  }
  .until--then  { left: 100px; top: 2320px; }
  .until--enjoy { left: 250px; top: 2425px; }

  .today {
    position: absolute;
    left: 150px;
    top: 2520px;
    margin: 0;
    font-family: "Gochi Hand", cursive;
    color: var(--sky);
    font-size: 270px;
    line-height: 1;
    letter-spacing: 14px;
    transform: skewX(-10deg);
    white-space: nowrap;
  }
</style>
</head>
<body>
<main class="ad">

  <svg class="speed-lines" width="420" height="960" viewBox="0 0 420 960" aria-hidden="true">
    <g fill="#ffffff">
      <polygon points="40,300 250,300 245,322 36,322"/>
      <polygon points="38,352 240,352 234,374 34,374"/>
      <polygon points="36,404 230,404 224,426 32,426"/>
      <polygon points="34,456 220,456 214,478 30,478"/>
      <polygon points="32,508 205,508 199,530 28,530"/>
      <polygon points="30,560 190,560 184,582 26,582"/>
      <polygon points="28,626 175,626 169,648 24,648"/>
      <polygon points="26,678 160,678 154,700 22,700"/>
      <polygon points="24,730 145,730 139,752 20,752"/>
      <polygon points="22,782 130,782 124,804 18,804"/>
      <polygon points="20,834 115,834 109,856 16,856"/>
      <polygon points="18,886 100,886 94,908 14,908"/>
    </g>
  </svg>

  <h1 class="headline headline--vegan">VEGAN</h1>
  <p class="headline headline--fast">FAST</p>
  <p class="headline headline--food">FOOD?</p>
  <span class="yep yep--food">YEP</span>

  <h2 class="question question--soon">COMING SOON ?</h2>
  <span class="yep yep--soon">YEP</span>

  <h2 class="question question--nyc">IN NYC</h2>
  <span class="yep yep--nyc">YEP</span>

  <p class="plea">In the name of all that<br>is good in the world...
    <span class="plea__where">Where ??</span>
  </p>

  <section class="contact-band">
    <p class="contact-band__site">www.<b>GreenDashEats</b>.com</p>
    <div class="contact-band__rule"></div>
    <p class="social social--one"><span class="social__mark"></span>/GreenDashEats</p>
    <p class="social social--two"><span class="social__mark"></span>@GreenDashEats</p>
  </section>

  <p class="until until--then">Until then...</p>
  <p class="until until--enjoy">enjoy our crispers</p>
  <p class="today">TODAY</p>

</main>
</body>
</html>
```